Quorvex business card design

create modern and tech looking business card that is clean but effectively communciates that we are a cloud communications company.
Should have at minimum:
Employee Name
Postion
Phone Number
Email
website
create modern and tech looking business card that is clean but effectively communciates that we are a cloud communications company. We have two logo color schemes (attached) so would like to see designs both ways
Should have at minimum:
Employee Name
Postion
Phone Number
Email
website

```html
<!DOCTYPE html>
<html lang="en">
<head>
<meta charset="UTF-8">
<title>Quorvex Business Card</title>
<link rel="stylesheet" href="https://fonts.googleapis.com/css2?family=Open+Sans:wght@400;600&display=swap">
<style>
  :root {
    --backdrop: #d3d3d3;
    --card-white: #ffffff;
    --brand-cyan: #2fb9d9;
    --brand-purple: #6a2f8f;
    --ink-dark: #3b3b40;
    --ink-grey: #6b6b70;
    --tint-purple: #ece4f3;
    --tint-cyan: #e3f4f9;
  }
  * { box-sizing: border-box; margin: 0; padding: 0; }
  html, body {
    width: 1200px; height: 800px; overflow: hidden;
    background: var(--backdrop);
    font-family: "Open Sans", Arial, sans-serif;
  }
  .stage {
    width: 1200px; height: 800px;
    display: flex; align-items: center; justify-content: center; gap: 60px;
  }
  .card {
    position: relative; width: 520px; height: 297px; overflow: hidden;
    box-shadow: 0 6px 18px rgba(0,0,0,0.18);
  }
  /* Front */
  .card-front { background: var(--card-white); }
  .name-band {
    position: absolute; left: 0; top: 112px; width: 330px; height: 56px;
    background: var(--brand-purple); color: #fff;
    padding: 9px 0 0 34px;
  }
  .name-band .person-name { font-size: 17px; font-weight: 400; letter-spacing: 0.5px; line-height: 1.2; }
  .name-band .person-role { font-size: 13px; line-height: 1.3; }
  .brand-lockup {
    position: absolute; left: 300px; top: 74px;
    display: flex; align-items: center; gap: 10px;
  }
  .brand-square { width: 22px; height: 22px; background: var(--brand-cyan); }
  .brand-name {
    font-size: 26px; font-weight: 600; letter-spacing: 3px; color: var(--ink-dark);
  }
  .decor-square {
    position: absolute; right: 40px; top: 150px; width: 120px; height: 120px;
    background: var(--tint-purple);
  }
  .contact-block {
    position: absolute; left: 34px; top: 190px;
    font-size: 12px; line-height: 1.45; color: var(--ink-grey);
  }
  .contact-block .address { margin-bottom: 8px; }
  .contact-block .label { color: var(--brand-purple); }
  /* Back */
  .card-back { background: var(--brand-cyan); }
  .back-lockup {
    position: absolute; left: 50%; top: 50%; transform: translate(-50%, -55%);
    display: flex; align-items: center; gap: 14px;
  }
  .back-lockup .brand-square { width: 34px; height: 34px; background: #fff; }
  .back-lockup .brand-name { font-size: 40px; color: #fff; letter-spacing: 4px; }
  .back-web {
    position: absolute; right: 30px; bottom: 22px;
    font-size: 11px; letter-spacing: 1px; color: #fff;
  }
</style>
</head>
<body>
<main class="stage">
  <section class="card card-front">
    <div class="decor-square"></div>
    <div class="brand-lockup">
      <span class="brand-square"></span>
      <span class="brand-name">QUORVEX</span>
    </div>
    <div class="name-band">
      <p class="person-name">DORIAN KELLS</p>
      <p class="person-role">Founder</p>
    </div>
    <div class="contact-block">
      <p class="address">4870 Larkspur Avenue,<br>Suite Tempe 85281</p>
      <p><span class="label">Cell:</span> 0455 907 318</p>
      <p><span class="label">Email:</span> info@doriankells.com</p>
      <p><span class="label">Web:</span> www.quorvex.com</p>
    </div>
  </section>

  <section class="card card-back">
    <div class="back-lockup">
      <span class="brand-square"></span>
      <span class="brand-name">QUORVEX</span>
    </div>
    <p class="back-web">www.quorvex.com</p>
  </section>
</main>
</body>
</html>
```